Business Consulting Company requires a website design (PSD+HTML+CSS required)

Marlowe Advisory is a Business Consulting Company that provides Analysis, Business Coaching and Systems and Document Design for clients.

We would like a simplistic yet professional looking website design that uses high quality imagery to project a professional persona across our entire site.

The completed project will need to include PSD files (for editing in Photoshop) and will need to also include HTML+CSS coded files that can be edited in Adobe Dreamweaver CS5.5.

Marlowe Advisory currently has a functioning website (located at www.marloweadvisory-example.com.au) but would like to replace its current site with something more professional, user friendly and content simplistic, with the overall design of this project being clean and very easy to navigate whilst remaining professionally focused.

A brief has been attached to this project to provide the key details but please feel free to contact me if you require any clarification or have any questions regarding the project.

Target Market(s)

The target audience for this website will be small to medium sized businesses (of all descriptions).

Industry/Entity Type

Business

Coding

Coded - Design and coding required

Number of Pages Required

5+ page

Requirements
Must have
• Simplistic design structure
• Professional images
• Easy to navigate
• Must be uploaded in PSD format
• Must be coded (HTML+CSS) and compatible with Adobe Dreamweaver CS5.5
Nice to have
• Use of the Company’s corporate colours throughout the site design
• Adding a Home page slider bar with images and short catchy messages (i.e. text based statements)
• Having a quick link box on each page that provides easy navigation throughout the site
• The use of different icons and images to depict our different services (i.e. a different icon and image for analysis service and coaching service etc.).
• All pages should follow a similar theme (universal approach to all pages)
Should not have
• When coding, images should not be used in place of text (all text must be editable)

```html
<!DOCTYPE html>
<html lang="en">
<head>
<meta charset="utf-8">
<title>Marlowe Advisory</title>
<link href="https://fonts.googleapis.com/css2?family=Arimo:wght@400;700&family=Open+Sans:wght@400;600;700&family=Raleway:wght@300;400;500&display=swap" rel="stylesheet">
<style>
:root{
  --blue:#1a9ad6;
  --blue-dark:#0f86c0;
  --ink:#2b2b2b;
  --text:#333;
  --grey-text:#555;
  --band:#efefef;
  --footer:#2c2c2c;
  --nav-active:#5a5d60;
  --icon:#222;
  --white:#fff;
}
*{margin:0;padding:0;box-sizing:border-box}
html,body{width:774px;height:1200px;overflow:hidden;background:var(--white)}
body{font-family:"Arimo",Arial,sans-serif;color:var(--text);position:relative}
.site-header{position:absolute;left:0;top:0;width:774px;height:73px}
.brand{position:absolute;left:65px;top:20px;display:flex;align-items:center;gap:10px}
.brand-mark{width:30px;height:30px;border-radius:50%;background:var(--blue)}
.brand-name{font-family:"Raleway",sans-serif;font-weight:400;font-size:21px;color:#555;letter-spacing:.5px}
.call{position:absolute;right:65px;top:27px;display:flex;align-items:center;gap:6px;font-family:"Open Sans",sans-serif;font-weight:600}
.call-label{color:var(--blue);font-size:15px}
.call-number{color:var(--ink);font-size:16px;margin-left:4px}
.main-nav{position:absolute;left:0;top:73px;width:774px;height:29px;background:var(--blue)}
.main-nav ul{list-style:none;display:flex;position:absolute;left:63px;top:6px}
.main-nav li{font-size:9.6px;color:var(--white);padding:4px 10px;margin-right:10px;line-height:11px}
.main-nav li.active{background:var(--nav-active)}
.hero{position:absolute;left:0;top:102px;width:774px;height:301px;background:linear-gradient(100deg,#c9ccd0 0%,#e3e4e2 30%,#7d8591 55%,#2d3340 75%,#d8dcdf 100%)}
.hero-caption{position:absolute;left:0;bottom:0;width:774px;height:66px;background:rgba(50,50,50,.55);color:var(--white);padding:3px 65px 0}
.hero-caption h1{font-family:"Raleway",sans-serif;font-weight:300;font-size:27px;line-height:32px}
.hero-caption p{font-size:9.4px;line-height:13px;width:570px}
.welcome{position:absolute;left:67px;top:443px;width:640px}
.welcome h2{font-family:"Open Sans",sans-serif;font-weight:600;font-size:19px;color:var(--ink)}
.welcome h2 span{color:#666}
.welcome h2 b{color:var(--blue);font-weight:600}
.welcome p{width:423px;font-size:9.5px;line-height:13px;margin-top:9px;text-align:justify;color:#222}
.video{position:absolute;left:520px;top:462px;width:185px;height:130px;border:2px solid #222;background:linear-gradient(135deg,#e8ecef,#8d96a2 60%,#c7ccd2)}
.video .play{position:absolute;left:78px;top:51px;width:28px;height:26px;background:rgba(30,30,30,.7)}
.video .bar{position:absolute;left:0;bottom:0;width:100%;height:14px;background:#d9d9d9;font-size:6px;color:#333;display:flex;align-items:center;gap:6px;padding:0 5px}
.video .track{flex:1;height:2px;background:#888}
.services{position:absolute;left:0;top:641px;width:774px;height:248px;background:var(--band)}
.service{position:absolute;top:40px;width:190px;text-align:center}
.service-icon{display:block;margin:0 auto;width:56px;height:56px}
.service h3{font-family:"Raleway",sans-serif;font-weight:400;font-size:17px;color:var(--blue);margin-top:12px;letter-spacing:.5px}
.service p{font-family:"Raleway",sans-serif;font-size:8.4px;line-height:13px;color:var(--grey-text);margin-top:5px}
.btn{display:inline-block;margin-top:13px;background:var(--blue);color:var(--white);font-size:8px;border:2px solid var(--blue-dark);border-radius:6px;padding:4px 10px;box-shadow:0 0 0 1px #8ccff0}
.divider{position:absolute;top:45px;width:1px;height:190px;background:#d6d6d6}
.testimonials{position:absolute;left:0;top:920px;width:774px;text-align:center}
.testimonials h2{font-family:"Raleway",sans-serif;font-weight:500;font-size:19px;color:#444}
.avatar{width:56px;height:56px;border-radius:50%;margin:12px auto 0;background:linear-gradient(#8a8f96,#3d4046);border:3px solid #e6e6e6}
.person{font-size:8.4px;font-weight:700;color:#444;margin-top:7px}
.quote{width:610px;margin:10px auto 0;font-size:9.6px;line-height:15px;color:#555;position:relative}
.quote .mark{font-family:"Open Sans",sans-serif;font-weight:700;font-size:20px;color:#444;position:absolute;line-height:1}
.site-footer{position:absolute;left:0;top:1122px;width:774px;height:78px;background:var(--footer);border-top:4px solid var(--blue)}
.footer-nav{list-style:none;display:flex;justify-content:center;margin-top:12px;font-size:8px;color:var(--white)}
.footer-nav li+li::before{content:"|";margin:0 12px}
.footer-rule{position:absolute;left:95px;top:30px;width:586px;height:2px;background:#111}
.copyright{position:absolute;left:0;top:43px;width:774px;display:flex;justify-content:center;align-items:center;gap:6px;color:var(--white);font-size:8.4px}
.social{display:flex;gap:3px;margin-left:4px}
.social span{width:16px;height:16px;border-radius:50%;background:#e8e8e8}
</style>
</head>
<body>
<header class="site-header">
  <div class="brand"><span class="brand-mark"></span><span class="brand-name">MARLOWE ADVISORY</span></div>
  <div class="call">
    <svg width="18" height="18" viewBox="0 0 18 18"><circle cx="9" cy="9" r="9" fill="#1a9ad6"/><path d="M6 4.5l2 2-1 1.3c.6 1.3 1.6 2.3 2.9 2.9l1.3-1 2 2-1.3 1.5C8.9 13 5 9.1 4.7 5.8z" fill="#fff"/></svg>
    <span class="call-label">Call Now !</span><span class="call-number">865 555-0142</span>
  </div>
</header>
<nav class="main-nav">
  <ul><li class="active">HOME</li><li>ABOUT US</li><li>CAPABILITIES</li><li>MISSION</li><li>NEWS</li><li>PHOTOS</li><li>CONTACT</li></ul>
</nav>
<section class="hero" role="img" aria-label="Photo of smiling consultants meeting around a table in a bright office">
  <div class="hero-caption">
    <h1>Grow Your Business</h1>
    <p>Lorem ipsum dolor sit amet, consectetur adipisicing elit, sed do eiusmod tempor incididunt ut labore et dolore magna aliqua. Ut enim ad minim veniam, quis nostrud exercitation ullamco laboris nisi ut aliquip ex ea commodo consequat.</p>
  </div>
</section>
<section class="welcome">
  <h2>Welcome to <span>M<b>A</b>RLOWE</span></h2>
  <p>It has survived not only five decidus centuries, but also the leap into electronic nelimp typesetting, remaining essentially unchanged.<br>It was popularised in the 1960s with the release of Letraset sheets containing lorem Ipsum passages, and more recently with desktop publishing software like<br>Lorem Ipsum is simply dummy text of the printing and typesetting industry. Lorem Ipsum has been the industry's standard dummy text ever since the 1500s, when an unknown printer took a galley.Phasellus adipiscing euismod tristique. Vestibulum non elit vitae enim interdum aliquam sed eget lacus. Phasellus egestas augue sed labore et dolore magna aliqua. Ut enim ad minim veniam, quis nostrud exercitau.</p>
</section>
<div class="video" role="img" aria-label="Video still of a business team shaking hands at a meeting">
  <div class="play"><svg width="28" height="26"><path d="M11 8l8 5-8 5z" fill="#fff"/></svg></div>
  <div class="bar"><span>&#9654;</span><span>00:00</span><span class="track"></span><span>00:00</span></div>
</div>
<section class="services">
  <div class="service" style="left:55px">
    <svg class="service-icon" viewBox="0 0 56 56"><g fill="#222"><rect x="8" y="32" width="9" height="18"/><rect x="23" y="22" width="9" height="28"/><rect x="38" y="12" width="9" height="38"/></g><rect x="5" y="51" width="46" height="2" fill="#1a9ad6"/></svg>
    <h3>LOREM IPSUM</h3>
    <p>Lorem ipsum dolor sit amet, consectetur exer-citation ullamco laboris nisi ut aliquip Ex-cepteur sint occaecat cupidatat non proident, sunt in culpa qui officia deserunt mollit anim id est laborum.</p>
    <span class="btn">LEARN MORE</span>
  </div>
  <div class="divider" style="left:265px"></div>
  <div class="service" style="left:283px">
    <svg class="service-icon" viewBox="0 0 56 56"><circle cx="28" cy="28" r="22" fill="none" stroke="#222" stroke-width="4"/><circle cx="28" cy="28" r="13" fill="none" stroke="#222" stroke-width="4"/><circle cx="28" cy="28" r="5" fill="#1a9ad6"/></svg>
    <h3>LOREM IPSUM</h3>
    <p>Lorem ipsum dolor sit amet, consectetur exer-citation ullamco laboris nisi ut aliquip Ex-cepteur sint occaecat cupidatat non proident, sunt in culpa qui officia deserunt mollit anim id est laborum.</p>
    <span class="btn">LEARN MORE</span>
  </div>
  <div class="divider" style="left:502px"></div>
  <div class="service" style="left:525px">
    <svg class="service-icon" viewBox="0 0 56 56"><rect x="8" y="8" width="40" height="40" rx="4" fill="none" stroke="#222" stroke-width="4"/><path d="M17 28l8 8 14-16" fill="none" stroke="#1a9ad6" stroke-width="4"/></svg>
    <h3>LOREM IPSUM</h3>
    <p>Lorem ipsum dolor sit amet, consectetur exer-citation ullamco laboris nisi ut aliquip Ex-cepteur sint occaecat cupidatat non proident, sunt in culpa qui officia deserunt mollit anim id est laborum.</p>
    <span class="btn">LEARN MORE</span>
  </div>
</section>
<section class="testimonials">
  <h2>OUR TESTIMONIALS</h2>
  <div class="avatar" role="img" aria-label="Portrait photo of the client giving the testimonial"></div>
  <div class="person">Mr Daniel Reeve</div>
  <p class="quote"><span class="mark" style="left:-18px;top:-3px">&ldquo;</span>A wonderful serenity has taken possession of my entire soul, like these sweet mornings of spring which I enjoy with my whole heartle heart. I am alone, and feel the charm of existence in this spot, which was created for the I am alone, and feel the charm of existence in this spot, which was created for the bliss of souls like mine. I am so happy.<span class="mark" style="position:relative;top:6px;margin-left:6px">&rdquo;</span></p>
</section>
<footer class="site-footer">
  <ul class="footer-nav"><li>HOME</li><li>ABOUT</li><li>SERVICES</li><li>PRODUCTS</li><li>OPPORTUNITIES</li><li>HIRE</li><li>INFORMATION</li><li>CONTACT</li></ul>
  <div class="footer-rule"></div>
  <div class="copyright">Copyright 2014 @ marloweadvisory-example.com<span class="social"><span></span><span></span><span></span><span></span></span></div>
</footer>
</body>
</html>
```